CD cover "Marisol Quintero"

Here I send the pictures for the cover, leaving creative freedom to the photography and any modifications you make. The artist is called Marisol Quintero, and the title of the album is called. "Over Quiet Rivers" but please translate that to Spanish. Thank you for your valuable work.
The name of the artist is: Marisol Quintero
Album Name: “Sobre ríos quietos” in Spanish

```html
<!DOCTYPE html>
<html lang="es">
<head>
<meta charset="utf-8">
<title>Marisol Quintero – Sobre ríos quietos</title>
<link rel="stylesheet" href="https://fonts.googleapis.com/css2?family=Bebas+Neue&family=Yellowtail&display=swap">
<style>
  :root {
    --page-bg: #ffffff;
    --sky-teal: #2f6f66;
    --sky-green: #5f8f6a;
    --haze-peach: #e9c9a8;
    --warm-red: #9a3a2c;
    --ember-orange: #c8672f;
    --dusk-purple: #4a2d5c;
    --night-navy: #1f2340;
    --flare-gold: #ffe08a;
    --script-yellow: #f2c94c;
    --title-lilac: #e6dcf7;
    --title-glow: rgba(170, 140, 255, 0.6);
    --badge-black: #111111;
    --badge-white: #ffffff;
  }
  * { margin: 0; padding: 0; box-sizing: border-box; }
  html, body {
    width: 1200px;
    height: 997px;
    overflow: hidden;
    background: var(--page-bg);
  }
  .album-cover {
    position: absolute;
    left: 150px;
    top: 48px;
    width: 900px;
    height: 900px;
    overflow: hidden;
  }
  .cover-photo {
    position: absolute;
    inset: 0;
    background:
      radial-gradient(circle at 72% 26%, var(--flare-gold) 0, rgba(255,224,138,0.55) 6%, rgba(255,224,138,0) 22%),
      radial-gradient(ellipse at 60% 8%, var(--haze-peach) 0, rgba(233,201,168,0) 45%),
      radial-gradient(ellipse at 30% 12%, var(--sky-teal) 0, rgba(47,111,102,0) 50%),
      radial-gradient(ellipse at 10% 55%, var(--warm-red) 0, rgba(154,58,44,0) 55%),
      radial-gradient(ellipse at 40% 62%, var(--ember-orange) 0, rgba(200,103,47,0) 40%),
      radial-gradient(ellipse at 85% 60%, var(--sky-green) 0, rgba(95,143,106,0) 45%),
      linear-gradient(180deg, var(--night-navy) 0%, var(--sky-teal) 30%, var(--warm-red) 60%, var(--dusk-purple) 100%);
  }
  .advisory-badge {
    position: absolute;
    left: 56px;
    top: 53px;
    width: 100px;
    height: 66px;
    background: var(--badge-black);
    border: 3px solid var(--badge-white);
  }
  .artist-name {
    position: absolute;
    left: 0;
    right: 0;
    top: 640px;
    text-align: center;
    font-family: "Yellowtail", cursive;
    font-size: 80px;
    line-height: 1;
    color: var(--script-yellow);
    transform: translateX(20px);
    white-space: nowrap;
  }
  .album-title {
    position: absolute;
    left: 0;
    right: 0;
    top: 736px;
    text-align: center;
    font-family: "Bebas Neue", sans-serif;
    font-weight: 400;
    font-size: 116px;
    line-height: 1;
    letter-spacing: 1px;
    color: var(--title-lilac);
    text-shadow: 0 0 18px var(--title-glow);
    white-space: nowrap;
  }
</style>
</head>
<body>
  <main class="album-cover">
    <div class="cover-photo" role="img" aria-label="Soft-focus portrait of the singer looking down, hair loose, in a denim shirt, set against a hazy teal, red and purple sky with bokeh lights, a sun flare and small birds"></div>
    <div class="advisory-badge" role="img" aria-label="Content advisory badge"></div>
    <p class="artist-name">Marisol Quintero</p>
    <h1 class="album-title">SOBRE RÍOS QUIETOS</h1>
  </main>
</body>
</html>
```